Looking for Desginers for an abstract art canvas & poster shopify shop

I want to get a design done for an abstract canvas art & print shop. If possible im looking to create the design based on the lumen or minimal template (im open to suggestions). Mostly I need the creative assets such as banners, images, copywriting, typography etc since im having a hard time to give it a descent look myself.

Target Market(s)

Home decor lovers, abstract art enthusiasts and canvas art enthusiast

Industry/Entity Type

Art

Coding

Coded - Design and coding required

Number of Pages Required

1 page

Colors

Designer to choose only greyscale colors for use in the design.

Requirements
Must have
• Creatives Assets such as banners, images, copy, collection image templates. Please use the velorin logo provided below in at least one of the proposals.
Should not have
• anything that has to be coded into html or css.

```html
<!DOCTYPE html>
<html lang="en">
<head>
<meta charset="utf-8">
<title>velorin — Abstract Canvas &amp; Posters</title>
<link href="https://fonts.googleapis.com/css2?family=Lora:ital,wght@0,400;0,600;1,400&display=swap" rel="stylesheet">
<style>
:root{
  --ink:#111;
  --text:#2b2b2b;
  --muted:#8a8a8a;
  --paper:#fff;
  --cream:#f7f6f4;
  --card:#f3f1ee;
  --blush:#ede3de;
  --rust:#9a4a22;
  --line:#1a1a1a;
  --gold:#e8c21a;
  --serif:'Lora', Georgia, serif;
}
*{margin:0;padding:0;box-sizing:border-box}
html,body{width:1200px;height:4508px;overflow:hidden}
body{position:relative;background:var(--paper);font-family:var(--serif);color:var(--text)}
.abs{position:absolute}
.center{left:0;width:1200px;text-align:center}
.rule{position:absolute;height:2px;background:var(--line);width:53px}
.btn-dark{position:absolute;background:var(--ink);color:#fff;font-size:12px;letter-spacing:.5px;display:flex;align-items:center;justify-content:center}
.btn-line{position:absolute;border:1.5px solid var(--ink);color:var(--ink);font-size:11px;display:flex;align-items:center;justify-content:center}
.fill{position:absolute}
.tile-label{position:absolute;color:#fff;font-size:15px}
.caption-title{position:absolute;text-align:center;font-size:18px;letter-spacing:6px;color:var(--ink)}
.caption-sub{position:absolute;text-align:center;font-size:12px;letter-spacing:5px;color:var(--ink)}
.section-title{position:absolute;font-size:32px;color:var(--ink)}
.section-sub{position:absolute;font-size:14px;font-style:italic;color:var(--text)}
.stars{position:absolute;color:var(--gold);font-size:14px;letter-spacing:1px;text-align:right;width:90px}
.reviews{position:absolute;color:#fff;font-size:11px;text-align:right;width:90px}
.footer-link{position:absolute;color:#fff;font-size:12px}
.body-copy{position:absolute;width:345px;font-size:12.5px;line-height:21.5px}
</style>
</head>
<body>

<section class="hero">
  <div class="fill" role="img" aria-label="Marbled paint swirls in pale blue, white and golden yellow" style="left:0;top:0;width:1200px;height:562px;background:
    radial-gradient(ellipse 160px 60px at 330px 300px,rgba(240,190,60,.55),transparent 70%),
    radial-gradient(ellipse 120px 40px at 560px 160px,rgba(240,200,80,.45),transparent 70%),
    radial-gradient(ellipse 420px 130px at 620px 120px,#b9cde0,transparent 70%),
    radial-gradient(ellipse 380px 160px at 900px 380px,#bfd2e4,transparent 70%),
    radial-gradient(ellipse 300px 120px at 180px 470px,#c8d8e6,transparent 70%),
    radial-gradient(ellipse 260px 120px at 800px 240px,#f5f6f6,transparent 70%),
    linear-gradient(135deg,#dfe8f0 0%,#f2f4f5 35%,#c9d8e6 60%,#eef1ef 80%,#d4e0ea 100%)"></div>
  <svg class="abs" style="left:172px;top:27px" width="20" height="16" viewBox="0 0 20 16"><path d="M1 2H19M1 8H19M1 14H19" stroke="#222" stroke-width="1.6"/></svg>
  <div class="abs center" style="top:16px;font-size:26px;font-style:italic;color:var(--ink)">velorin</div>
  <svg class="abs" style="left:885px;top:25px" width="18" height="18" viewBox="0 0 18 18"><circle cx="7.5" cy="7.5" r="5.5" fill="none" stroke="#222" stroke-width="1.6"/><path d="M11.5 11.5L16.5 16.5" stroke="#222" stroke-width="1.6"/></svg>
  <svg class="abs" style="left:946px;top:25px" width="20" height="18" viewBox="0 0 20 18"><path d="M1 2H4L6 12H16L18 5H5" fill="#222" stroke="#222" stroke-width="1.4"/><circle cx="7" cy="15.5" r="1.6" fill="#222"/><circle cx="15" cy="15.5" r="1.6" fill="#222"/></svg>
  <svg class="abs" style="left:1008px;top:25px" width="18" height="18" viewBox="0 0 18 18"><rect x="1" y="3" width="10" height="12" fill="none" stroke="#222" stroke-width="1.4"/><rect x="7" y="5" width="10" height="12" fill="#fff" stroke="#222" stroke-width="1.4"/></svg>
  <h1 class="abs center" style="top:226px;font-size:38px;font-weight:400;color:var(--ink)">Get Your Aesthetic Enjoyment</h1>
  <div class="btn-dark" style="left:532px;top:296px;width:136px;height:38px">EXPLORE NOW</div>
  <div class="abs" style="left:173px;top:489px;font-size:15px;color:var(--ink);border-bottom:1.5px solid var(--ink);padding-bottom:3px">CANVAS</div>
  <div class="abs" style="left:949px;top:489px;font-size:15px;color:var(--ink);border-bottom:1.5px solid var(--ink);padding-bottom:3px">POSTERS</div>
</section>

<section class="passion">
  <div class="fill" style="left:600px;top:562px;width:600px;height:528px;background:var(--cream)"></div>
  <div class="fill" style="left:124px;top:653px;width:352px;height:350px;background:var(--card)"></div>
  <div class="fill" role="img" aria-label="Black canvas with two sweeping white brush strokes" style="left:210px;top:670px;width:180px;height:245px;background:
    radial-gradient(ellipse 90px 28px at 130px 55px,#f2f2f2,transparent 75%),
    radial-gradient(ellipse 110px 26px at 60px 210px,#e6e6e6,transparent 75%),
    #0c0c0c"></div>
  <div class="caption-title" style="left:124px;width:352px;top:933px;font-size:16px">Black &amp; White</div>
  <div class="caption-sub" style="left:124px;width:352px;top:962px;font-size:11px">• Abstract Art •</div>
  <div class="rule" style="left:686px;top:692px"></div>
  <h2 class="abs" style="left:686px;top:706px;font-size:28px;font-weight:400;font-style:italic;line-height:36px;color:var(--ink)">Artwork made out<br>of passion</h2>
  <p class="body-copy" style="left:686px;top:806px">Our products are inspired by the people and world around us. Beautiful, high quality arts and posters that are designed especially for you. Discover <span style="color:var(--muted)">our story</span> and meet the people that make our brand what it is.</p>
  <div class="btn-line" style="left:686px;top:924px;width:121px;height:36px">LEARN MORE</div>
</section>

<section class="video">
  <div class="fill" role="img" aria-label="Grey streaked brush texture with billowing white paint clouds" style="left:0;top:1090px;width:1200px;height:438px;background:
    radial-gradient(ellipse 170px 110px at 820px 280px,#e2e2df,transparent 70%),
    radial-gradient(ellipse 160px 90px at 330px 300px,#dadad7,transparent 70%),
    radial-gradient(ellipse 140px 80px at 1080px 300px,#d8d8d4,transparent 70%),
    radial-gradient(ellipse 120px 70px at 80px 320px,#d4d4d0,transparent 70%),
    linear-gradient(180deg,#858583 0%,#a9a9a6 45%,#c9c9c6 75%,#b8b8b5 100%)"></div>
  <div class="abs center" style="top:1262px;font-size:36px;font-style:italic;line-height:46px;color:var(--ink)">View the best,<br>by the best</div>
  <svg class="abs" style="left:551px;top:1261px" width="96" height="96" viewBox="0 0 96 96"><circle cx="48" cy="48" r="46" fill="none" stroke="#fff" stroke-width="2.5"/><path d="M40 34L62 48L40 62Z" fill="#fff"/></svg>
</section>

<section class="styles">
  <div class="rule" style="left:573px;top:1602px"></div>
  <h2 class="section-title center" style="top:1614px;font-weight:400">Search by Style</h2>
  <p class="section-sub center" style="top:1670px">The best artworks you'll encounter</p>
  <div class="fill" role="img" aria-label="Bare dark tree in a grey misty field" style="left:0;top:1764px;width:400px;height:280px;background:radial-gradient(ellipse 70px 80px at 200px 130px,#3a3a3a,transparent 75%),linear-gradient(180deg,#5e5e5e,#6c6c6c 70%,#787878)"></div>
  <div class="fill" role="img" aria-label="Dark green striped tropical leaves" style="left:400px;top:1764px;width:400px;height:280px;background:radial-gradient(ellipse 110px 70px at 110px 70px,#4d7564,transparent 75%),radial-gradient(ellipse 120px 80px at 300px 200px,#3f6656,transparent 75%),linear-gradient(135deg,#2d4a3e,#14211b 60%,#2f4c40)"></div>
  <div class="fill" role="img" aria-label="Wall of torn colourful street posters" style="left:800px;top:1764px;width:400px;height:280px;background:radial-gradient(ellipse 60px 90px at 90px 120px,#6f6660,transparent 75%),radial-gradient(ellipse 60px 70px at 330px 60px,#7a3a44,transparent 75%),linear-gradient(90deg,#45454a,#5e5350 50%,#35323a)"></div>
  <div class="tile-label" style="left:0;width:400px;top:1894px;text-align:center;font-style:italic">Black &amp; White</div>
  <div class="tile-label" style="left:400px;width:400px;top:1894px;text-align:center;font-style:italic">Natural</div>
  <div class="tile-label" style="left:800px;width:400px;top:1894px;text-align:center;font-style:italic">Posters</div>
</section>

<section class="feel">
  <div class="fill" style="left:0;top:2044px;width:1200px;height:438px;background:var(--cream)"></div>
  <div class="rule" style="left:175px;top:2125px"></div>
  <h2 class="abs" style="left:175px;top:2140px;font-size:28px;font-weight:400;font-style:italic;color:var(--ink)">Feel our ArtWork</h2>
  <p class="body-copy" style="left:175px;top:2204px">Lorem ipsum dolor sit amet, consetetur sadipscing elitr, sed diam nonumy eirmod tempor invidunt ut labore et dolore magna aliquyam erat, sed diam voluptua. At vero eos et accusam et justo duo dolores et ea rebum. Stet clita kasd gubergren, no sea takimata sanctus est Lorem ipsum dolor sit amet. Lorem ipsum dolor sit amet, consetetur</p>
  <div class="btn-line" style="left:175px;top:2364px;width:102px;height:37px">VIEW ALL</div>
  <div class="fill" role="img" aria-label="Two overlapping rust brown line drawn shapes on blush" style="left:691px;top:2090px;width:277px;height:283px;background:
    radial-gradient(ellipse 70px 80px at 110px 110px,rgba(154,74,34,.28),transparent 72%),
    radial-gradient(ellipse 60px 70px at 170px 190px,rgba(154,74,34,.3),transparent 72%),
    var(--blush)"></div>
  <div class="caption-title" style="left:640px;width:380px;top:2386px">Connection Modern</div>
  <div class="caption-sub" style="left:640px;width:380px;top:2418px">• Abstract Art •</div>
</section>

<section class="featured">
  <div class="rule" style="left:573px;top:2556px"></div>
  <h2 class="section-title center" style="top:2569px;font-weight:400">Featured Collection</h2>
  <p class="section-sub center" style="top:2624px">Choose your favourite</p>
  <div class="fill" style="left:0;top:2718px;width:600px;height:749px;background:var(--cream)"></div>
  <div class="fill" role="img" aria-label="Black continuous line drawing of a figure on blush" style="left:119px;top:2863px;width:362px;height:373px;background:
    radial-gradient(ellipse 90px 150px at 150px 190px,rgba(20,20,20,.12),transparent 72%),
    radial-gradient(ellipse 70px 60px at 250px 300px,rgba(20,20,20,.1),transparent 72%),
    var(--blush)"></div>
  <div class="caption-title" style="left:100px;width:400px;top:3256px;font-size:22px;letter-spacing:8px">Simplicity Line</div>
  <div class="caption-sub" style="left:100px;width:400px;top:3295px;font-size:14px">• Abstract Art •</div>

  <div class="fill" role="img" aria-label="Lilac, white and blue marbled fluid paint" style="left:600px;top:2718px;width:600px;height:250px;background:radial-gradient(ellipse 160px 60px at 420px 80px,#ece6f0,transparent 70%),radial-gradient(ellipse 180px 70px at 180px 170px,#4a4f7d,transparent 70%),linear-gradient(135deg,#8b8fb3,#c8c2d8 40%,#5c6290 70%,#b4aed0)"></div>
  <div class="fill" role="img" aria-label="Colourful abstract painting in orange, navy, black and cream" style="left:600px;top:2968px;width:600px;height:250px;background:radial-gradient(ellipse 130px 90px at 500px 100px,#ece2c2,transparent 72%),radial-gradient(ellipse 120px 40px at 200px 160px,#1a1a1a,transparent 72%),linear-gradient(120deg,#1d3a55,#c77a1a 35%,#d69a2a 65%,#c98a22)"></div>
  <div class="fill" role="img" aria-label="Layered torn classic posters on a wall" style="left:600px;top:3218px;width:600px;height:249px;background:radial-gradient(ellipse 120px 90px at 470px 110px,#e6dfcc,transparent 70%),radial-gradient(ellipse 100px 80px at 150px 120px,#8a8a8a,transparent 70%),linear-gradient(90deg,#3c3c40,#6a6a6c 50%,#2f3e55)"></div>

  <div class="tile-label" style="left:630px;top:2932px;font-size:14px">Wall Art</div>
  <div class="stars" style="left:1079px;top:2920px">★★★★★</div>
  <div class="reviews" style="left:1073px;top:2938px">(20 reviews)</div>
  <div class="tile-label" style="left:630px;top:3182px;font-size:14px">Colourful Abstract</div>
  <div class="stars" style="left:1079px;top:3170px">★★★★★</div>
  <div class="reviews" style="left:1073px;top:3188px">(20 reviews)</div>
  <div class="tile-label" style="left:630px;top:3432px;font-size:14px">Classic Posters</div>
  <div class="stars" style="left:1079px;top:3420px">★★★★★</div>
  <div class="reviews" style="left:1073px;top:3438px">(20 reviews)</div>
</section>

<section class="product">
  <div class="fill" role="img" aria-label="Black and white abstract brush strokes artwork" style="left:231px;top:3544px;width:301px;height:400px;background:radial-gradient(ellipse 170px 60px at 150px 60px,#f0f0f0,transparent 75%),linear-gradient(170deg,#dcdcdc 0%,#7a7a7a 28%,#2a2a2a 50%,#161616 100%)"></div>
  <h2 class="abs" style="left:579px;width:400px;top:3541px;text-align:center;font-size:28px;font-weight:600;color:var(--ink)">Abstract Strokes</h2>
  <div class="abs" style="left:579px;width:400px;top:3590px;text-align:center;font-size:14px;color:var(--muted)">$100</div>
  <div class="abs" style="left:607px;top:3703px;width:345px;height:37px;background:#dcdcdc;display:flex;align-items:center;justify-content:space-between;padding:0 18px;font-size:13px;color:#555">Variations<svg width="10" height="6" viewBox="0 0 10 6"><path d="M0 0H10L5 6Z" fill="#111"/></svg></div>
  <div class="btn-line" style="left:607px;top:3771px;width:345px;height:36px;font-size:12px">Add to Cart</div>
  <div class="btn-dark" style="left:607px;top:3827px;width:345px;height:36px;font-size:12px">Buy it Now</div>
  <svg class="abs" style="left:725px;top:3929px" width="26" height="16" viewBox="0 0 26 16"><path d="M0 2H3M7 2H26M0 8H3M7 8H26M0 14H3M7 14H26" stroke="#111" stroke-width="1.8"/></svg>
  <div class="abs" style="left:770px;top:3928px;font-size:12px;color:var(--ink)">Full Details</div>
</section>

<section class="cta">
  <div class="fill" role="img" aria-label="Pale grey speckled paint texture" style="left:0;top:4020px;width:1200px;height:250px;background:radial-gradient(ellipse 120px 90px at 170px 110px,#bdbdbd,transparent 72%),radial-gradient(ellipse 100px 80px at 1000px 150px,#c4c4c4,transparent 72%),linear-gradient(90deg,#dcdcdc,#f1f1f1 40%,#e8e8e8 70%,#d6d6d6)"></div>
  <h2 class="abs center" style="top:4080px;font-size:30px;font-weight:600;color:var(--ink)">Enjoy the Beauty of true Art</h2>
  <p class="abs center" style="top:4135px;font-size:12px;color:var(--text)">Discover great art and talent</p>
  <div class="btn-dark" style="left:532px;top:4170px;width:136px;height:39px">EXPLORE NOW</div>
</section>

<footer class="site-footer">
  <div class="fill" style="left:0;top:4270px;width:1200px;height:238px;background:#000"></div>
  <a class="footer-link" style="left:173px;top:4332px">Search</a>
  <a class="footer-link" style="left:173px;top:4357px">Articles</a>
  <a class="footer-link" style="left:173px;top:4382px">FAQs</a>
  <a class="footer-link" style="left:173px;top:4406px">Contact Us</a>
  <div class="footer-link" style="left:738px;top:4332px">SIGN UP FOR UPDATES</div>
  <div class="footer-link" style="left:738px;top:4361px;font-size:11px">Promotions, products and sales. Directly to your inbox.</div>
  <div class="abs" style="left:750px;top:4406px;font-size:9px;color:#888">Your email address</div>
  <div class="abs" style="left:955px;top:4405px;font-size:9px;color:#fff;letter-spacing:.5px">SUBSCRIBE ▸</div>
  <div class="fill" style="left:738px;top:4421px;width:289px;height:1px;background:#fff"></div>
  <div class="abs center" style="top:4477px;font-size:8px;color:#aaa">© 2021, velorin | All Rights Reserved</div>
</footer>

</body>
</html>
```